Design Catagory App Icons for Gearvo.com new app launching in 2020

We need the icons designed for our categories in our app that suit the colors and layout of the app. 20 icons that need doing for an APP menu see on the left of the image I have uploaded. On or the sliding menu on the left we have small icons that represent the master categories. The master categories are listed in column A in the spreadsheet provided and we need an icon for each category that would sit above the words and suit the apps design and flow and colors.

Target Market(s)

Men all ages

Industry/Entity Type

Retail

Requirements
Must have
• An icon for each category listed in the spreadsheet to be successful.
Nice to have
• All the icons work together in the same family
Should not have
• Don't combine too many colors

```html
<!DOCTYPE html>
<html lang="en">
<head>
<meta charset="utf-8">
<title>Gearvo.com – App Home</title>
<link rel="stylesheet" href="https://fonts.googleapis.com/css2?family=Montserrat:wght@500;600;700;800;900&display=swap">
<style>
:root{
  --page:#eeeeee;
  --chrome:#c8c8c8;
  --rail:#cbcbcb;
  --rail-line:#dcdcdc;
  --blue:#128bea;
  --ink:#1b1b1b;
  --muted:#8a8a8a;
  --price:#d0202b;
  --card-line:#cfcfcf;
  --white:#ffffff;
  --pill:#3a3f44;
}
*{margin:0;padding:0;box-sizing:border-box}
html,body{width:1200px;height:800px;overflow:hidden;background:var(--page);font-family:"Montserrat",sans-serif;color:var(--ink)}
.screen{position:absolute;left:398px;top:40px;width:505px;height:900px;transform:scale(.8);transform-origin:0 0;background:var(--white);overflow:hidden}
.abs{position:absolute}
.top-bar{left:0;top:0;width:505px;height:101px;background:var(--chrome)}
.status-time{left:36px;top:9px;font-size:10.5px;font-weight:600}
.status-icons{right:18px;top:12px}
.search{left:62px;top:66px;width:280px;height:26px;border-radius:13px;background:#ececec;display:flex;align-items:center;padding-left:12px;gap:10px;font-size:10px;font-weight:700}
.top-action{top:68px}
.rail{left:0;top:101px;width:88px;height:712px;background:var(--rail)}
.rail-item{position:absolute;left:0;width:88px;text-align:center;font-size:10px;font-weight:500;line-height:11px;text-transform:uppercase}
.rail-item svg{display:block;margin:0 auto 6px}
.rail-sep{position:absolute;left:0;width:88px;height:3px;background:var(--rail-line)}
.rail-featured{left:0;top:101px;width:88px;height:77px;background:var(--blue)}
.rail-tab{left:88px;top:101px}
.section-title{font-size:15px;font-weight:700;letter-spacing:.2px}
.see-all{width:64px;height:21px;border:1.5px solid #555;border-radius:5px;font-size:8px;font-weight:600;display:flex;align-items:center;justify-content:center}
.hero{left:148px;top:155px;width:298px;height:187px;border-radius:4px;background:radial-gradient(ellipse at 45% 55%,#6b2a26 0%,#3a1d1b 55%,#1e1616 100%);overflow:hidden}
.hero-title{left:0;top:38px;width:298px;text-align:center;color:var(--white);font-weight:900;font-size:44px;line-height:46px;letter-spacing:-1px}
.hero-dots{left:128px;top:167px;display:flex;gap:5px}
.hero-dots span{width:5px;height:5px;border-radius:50%;background:#888}
.hero-dots span:first-child{width:7px;height:7px;margin-top:-1px;background:#fff}
.hero-swipe{right:26px;top:166px;color:#fff;font-size:8px;font-weight:500}
.card{border:1.5px solid var(--card-line);border-radius:4px;background:var(--white);overflow:hidden}
.card-photo{position:absolute;border-radius:2px}
.card-cart{position:absolute;width:14px;height:14px;border-radius:3px;background:#999}
.card-name{position:absolute;font-size:9px;font-weight:600;line-height:11px;white-space:nowrap}
.card-price{position:absolute;font-size:12px;font-weight:700;color:var(--price);white-space:nowrap}
.card-price s{color:#aaa;font-weight:500;margin-left:6px}
.mini-price{font-size:9px}
.fade{left:88px;top:760px;width:417px;height:53px;background:linear-gradient(rgba(255,255,255,0),#fff)}
.filters{left:205px;top:773px;width:100px;height:32px;border-radius:16px;background:var(--pill);color:#fff;font-size:10px;font-weight:600;display:flex;align-items:center;justify-content:center;gap:8px}
.chat{left:384px;top:753px;width:52px;height:52px;border-radius:50%;background:var(--blue);display:flex;align-items:center;justify-content:center}
.nav{left:0;top:813px;width:505px;height:87px;background:var(--blue)}
</style>
</head>
<body>
<main class="screen">
  <header class="abs top-bar"></header>
  <div class="abs status-time">09:40 PM</div>
  <svg class="abs status-icons" width="90" height="18" viewBox="0 0 90 18">
    <g fill="#111"><rect x="0" y="12" width="2.5" height="4"/><rect x="4" y="9" width="2.5" height="7"/><rect x="8" y="6" width="2.5" height="10"/><rect x="12" y="3" width="2.5" height="13"/><rect x="16" y="0" width="2.5" height="16"/></g>
    <g fill="none" stroke="#111" stroke-width="2"><path d="M30 6a10 10 0 0 1 14 0"/><path d="M33 9a6 6 0 0 1 8 0"/></g><circle cx="37" cy="13" r="2" fill="#111"/>
    <rect x="58" y="3" width="27" height="12" rx="2" fill="none" stroke="#111" stroke-width="2"/><rect x="86" y="6.5" width="3" height="5" fill="#111"/>
    <g fill="#111"><rect x="61" y="6" width="6" height="6"/><rect x="68.5" y="6" width="6" height="6"/><rect x="76" y="6" width="6" height="6"/></g>
  </svg>
  <div class="abs search">
    <svg width="16" height="16" viewBox="0 0 16 16"><circle cx="6" cy="6" r="4.5" fill="none" stroke="#111" stroke-width="1.8"/><path d="M9.5 9.5l5 5" stroke="#111" stroke-width="2"/></svg>SEARCH
  </div>
  <svg class="abs top-action" style="left:404px" width="26" height="24" viewBox="0 0 26 24"><path d="M15 3l9 8-9 8v-5C8 14 4 16 1 21c1-8 5-12 14-13z" fill="#111"/></svg>
  <svg class="abs top-action" style="left:444px" width="24" height="24" viewBox="0 0 24 24"><path d="M1 3h4l3 11h11l3-8H7" fill="none" stroke="#111" stroke-width="2.4"/><path d="M7 6h15l-3 8H9z" fill="#111"/><circle cx="9.5" cy="19.5" r="2" fill="#111"/><circle cx="18" cy="19.5" r="2" fill="#111"/></svg>

  <nav class="abs rail" aria-label="Categories">
    <div class="rail-sep" style="top:154px"></div>
    <div class="rail-sep" style="top:229px"></div>
    <div class="rail-sep" style="top:307px"></div>
    <div class="rail-sep" style="top:387px"></div>
    <div class="rail-sep" style="top:461px"></div>
    <div class="rail-sep" style="top:539px"></div>
    <div class="rail-sep" style="top:617px"></div>

    <div class="rail-item" style="top:90px">
      <svg width="38" height="36" viewBox="0 0 38 36"><path d="M4 8l4-4 6 6-2 2 18 18-4 4L8 16l-2 2z" fill="#111"/><path d="M32 3l3 3-5 5 3 3-4 4-3-3L8 33l-4-2 1-3L23 10l-3-3 4-4 3 3z" fill="#111"/></svg>
      Powertools
    </div>
    <div class="rail-item" style="top:158px">
      <svg width="40" height="38" viewBox="0 0 40 38"><g fill="#111"><circle cx="20" cy="20" r="13"/><path d="M20 3l3 5h-6zM34 12l-2 6-4-4zM6 12l6 2-4 4z"/><rect x="8" y="26" width="24" height="6"/></g><circle cx="20" cy="20" r="3" fill="#cbcbcb"/></svg>
      Powertool<br>Accessories
    </div>
    <div class="rail-item" style="top:235px">
      <svg width="30" height="40" viewBox="0 0 30 40"><g fill="#111"><rect x="8" y="1" width="14" height="12" rx="2"/><rect x="13" y="13" width="4" height="20"/><rect x="6" y="18" width="18" height="4"/><rect x="4" y="34" width="22" height="5"/></g></svg>
      Benchtools &amp;<br>Woodworking
    </div>
    <div class="rail-item" style="top:317px">
      <svg width="50" height="38" viewBox="0 0 50 38"><path d="M4 2l14 20" stroke="#111" stroke-width="2.5"/><path d="M14 20h20l8 8H14z" fill="#111"/><circle cx="20" cy="31" r="5" fill="#111"/><circle cx="42" cy="32" r="5" fill="none" stroke="#111" stroke-width="2.5"/></svg>
      Outdoor
    </div>
    <div class="rail-item" style="top:390px">
      <svg width="48" height="38" viewBox="0 0 48 38"><g fill="#111"><rect x="4" y="8" width="40" height="24" rx="2"/><rect x="6" y="32" width="6" height="4"/><rect x="36" y="32" width="6" height="4"/><rect x="20" y="2" width="14" height="6"/></g><path d="M30 12l-5 8h4l-3 8 7-10h-4l3-6z" fill="#cbcbcb"/><rect x="8" y="14" width="10" height="3" fill="#cbcbcb"/></svg>
      Power &amp;<br>Lighting
    </div>
    <div class="rail-item" style="top:468px">
      <svg width="40" height="44" viewBox="0 0 40 44"><path d="M8 4l26 36" stroke="#111" stroke-width="4"/><path d="M32 4L8 40" stroke="#111" stroke-width="4"/><path d="M2 8l10-6 6 8-8 4zM26 2l10 2-2 10-6-2z" fill="#111"/></svg>
      Handtools
    </div>
    <div class="rail-item" style="top:544px">
      <svg width="30" height="42" viewBox="0 0 30 42"><g fill="none" stroke="#111" stroke-width="3"><path d="M6 2c-3 4 0 8 3 8l12 24"/><path d="M24 2c3 4 0 8-3 8L9 34"/><circle cx="8" cy="37" r="3.5"/><circle cx="22" cy="37" r="3.5"/></g></svg>
      Auto &amp;<br>Air Tools
    </div>
    <div class="rail-item" style="top:628px">
      <svg width="44" height="44" viewBox="0 0 44 44"><path d="M4 18h36v22H4z" fill="#111"/><path d="M8 18l6-14 4 2-4 12zM18 18l2-12h4l-2 12zM26 18l6-12 4 2-6 10z" fill="#111"/><rect x="16" y="24" width="12" height="4" fill="#cbcbcb"/></svg>
      Storage &amp;<br>Workshop
    </div>
  </nav>

  <div class="abs rail-featured"></div>
  <svg class="abs rail-tab" width="26" height="77" viewBox="0 0 26 77"><path d="M0 0h26L0 32z" fill="var(--blue)"/></svg>
  <div class="abs rail-item" style="top:110px;left:0">
    <svg width="38" height="36" viewBox="0 0 38 36"><path d="M4 6l3-3 16 16-3 3z" fill="#111"/><path d="M6 2L2 6l3 3 4-4z" fill="#111"/><path d="M30 2a7 7 0 0 0-6 9L6 29a3 3 0 0 0 4 4l18-18a7 7 0 0 0 9-6l-4 3-4-1-1-4z" fill="#111"/><path d="M20 23l10 10 3-3-10-10z" fill="#111"/></svg>
    Featured
  </div>

  <h2 class="abs section-title" style="left:159px;top:124px">TOOL OF THE DAY</h2>
  <div class="abs hero" role="img" aria-label="Workshop photo of a red cordless circular saw on a garage workbench">
    <div class="abs hero-title">TOOL OF<br>THE DAY</div>
    <div class="abs hero-dots"><span></span><span></span><span></span><span></span></div>
    <div class="abs hero-swipe">SWIPE FOR MORE</div>
  </div>

  <h2 class="abs section-title" style="left:159px;top:364px;font-size:14px">WEEKLY TOP TEN</h2>
  <div class="abs see-all" style="left:370px;top:363px">SEE ALL</div>

  <article class="abs card" style="left:148px;top:395px;width:128px;height:197px">
    <div class="card-photo" role="img" aria-label="Red and black cordless drill with battery" style="left:14px;top:10px;width:98px;height:112px;background:linear-gradient(160deg,#d62c2c,#3a2a2a 70%,#c92222)"></div>
    <div class="card-cart" style="right:6px;top:6px"></div>
    <p class="card-name" style="left:7px;top:133px">Forgeline X20 Cordless<br>Brushless 1/2 In. Drill/<br>Driver Kit</p>
    <p class="card-price" style="left:7px;top:172px">$89.00<s>$109.00</s></p>
  </article>
  <article class="abs card" style="left:281px;top:395px;width:128px;height:197px">
    <div class="card-photo" role="img" aria-label="Yellow and black cordless drill" style="left:8px;top:10px;width:104px;height:112px;background:linear-gradient(160deg,#f2c01c,#2a2a2a 70%,#f0b90f)"></div>
    <div class="card-cart" style="right:6px;top:6px"></div>
    <p class="card-name" style="left:7px;top:133px">Ironvale Surge<br>Lithium-Ion 1/2 In.<br>Cordless Driver-Drill</p>
    <p class="card-price" style="left:7px;top:172px">$89.00</p>
  </article>
  <article class="abs card" style="left:413px;top:395px;width:60px;height:197px">
    <div class="card-photo" role="img" aria-label="Black and red cordless nailer" style="left:6px;top:18px;width:34px;height:102px;background:linear-gradient(90deg,#222,#555 60%,#c22)"></div>
    <p class="card-name" style="left:5px;top:133px">Ironvale<br>Lithium<br>Cordless</p>
    <p class="card-price" style="left:5px;top:172px">$89.00</p>
  </article>

  <h2 class="abs section-title" style="left:159px;top:614px;font-size:14px">JUST DROPPED</h2>
  <div class="abs see-all" style="left:370px;top:613px">SEE ALL</div>

  <article class="abs card" style="left:148px;top:645px;width:95px;height:95px">
    <div class="card-photo" role="img" aria-label="Red compact screwdriver" style="left:14px;top:6px;width:60px;height:66px;background:linear-gradient(150deg,#d92a2a,#4a2626)"></div>
    <div class="card-cart" style="right:4px;top:4px;width:12px;height:12px"></div>
    <p class="card-price mini-price" style="left:6px;top:78px">$89.00<s>$89.00</s></p>
  </article>
  <article class="abs card" style="left:249px;top:645px;width:95px;height:95px">
    <div class="card-photo" role="img" aria-label="Yellow compact drill" style="left:14px;top:6px;width:64px;height:66px;background:linear-gradient(150deg,#f2c01c,#2b2b2b 75%)"></div>
    <div class="card-cart" style="right:4px;top:4px;width:12px;height:12px"></div>
    <p class="card-price mini-price" style="left:6px;top:78px">$89.00</p>
  </article>
  <article class="abs card" style="left:349px;top:645px;width:95px;height:95px">
    <div class="card-photo" role="img" aria-label="Teal compact drill" style="left:14px;top:6px;width:64px;height:66px;background:linear-gradient(150deg,#1d9aa0,#2b2b2b 75%)"></div>
    <div class="card-cart" style="right:4px;top:4px;width:12px;height:12px"></div>
    <p class="card-price mini-price" style="left:6px;top:78px">$89.00</p>
  </article>

  <article class="abs card" style="left:148px;top:745px;width:95px;height:95px">
    <div class="card-photo" role="img" aria-label="Yellow cordless drill" style="left:14px;top:8px;width:64px;height:70px;background:linear-gradient(150deg,#f2c01c,#2b2b2b 75%)"></div>
    <div class="card-cart" style="right:4px;top:4px;width:12px;height:12px"></div>
  </article>
  <article class="abs card" style="left:249px;top:745px;width:95px;height:95px">
    <div class="card-photo" role="img" aria-label="Teal cordless drill" style="left:14px;top:8px;width:64px;height:70px;background:linear-gradient(150deg,#1d9aa0,#2b2b2b 75%)"></div>
    <div class="card-cart" style="right:4px;top:4px;width:12px;height:12px"></div>
  </article>
  <article class="abs card" style="left:349px;top:745px;width:95px;height:95px">
    <div class="card-photo" role="img" aria-label="Red cordless tool" style="left:14px;top:8px;width:64px;height:70px;background:linear-gradient(150deg,#d92a2a,#4a2626)"></div>
    <div class="card-cart" style="right:4px;top:4px;width:12px;height:12px"></div>
  </article>

  <div class="abs fade"></div>
  <div class="abs filters">
    <svg width="14" height="10" viewBox="0 0 14 10"><g fill="#fff"><rect x="0" y="0" width="14" height="1.6"/><rect x="3" y="4" width="8" height="1.6"/><rect x="5.5" y="8" width="3" height="1.6"/></g></svg>FILTERS
  </div>
  <div class="abs chat">
    <svg width="24" height="22" viewBox="0 0 24 22"><path d="M3 1h18a2 2 0 0 1 2 2v12a2 2 0 0 1-2 2H8l-5 4v-4a2 2 0 0 1-2-2V3a2 2 0 0 1 2-2z" fill="#fff"/><g fill="var(--blue)"><rect x="6" y="6" width="12" height="1.6"/><rect x="6" y="9" width="12" height="1.6"/><rect x="6" y="12" width="8" height="1.6"/></g></svg>
  </div>

  <footer class="abs nav">
    <svg class="abs" style="left:70px;top:22px" width="44" height="42" viewBox="0 0 44 42"><path d="M42 0v42L0 21z" fill="#d9d9d9"/></svg>
    <div class="abs" style="left:239px;top:20px;width:46px;height:46px;border-radius:50%;background:#e2e2e2"></div>
    <svg class="abs" style="left:399px;top:25px" width="38" height="34" viewBox="0 0 38 34"><g fill="#e2e2e2"><rect y="0" width="38" height="6" rx="3"/><rect y="14" width="38" height="6" rx="3"/><rect y="28" width="38" height="6" rx="3"/></g></svg>
  </footer>
</main>
</body>
</html>
```